Brightkoru NZ Brand, Revenue, Promotions & Events

I need an innovative business card that pops my brand. I like the colours against darker gradients and i'm not afraid to be bold.

I run my own Business, Brand, Event & Promotion company. I specialise in breathing life into businesses and adding atmosphere to promotions and events. I am concept based lady that likes to test the boundaries and create stand out campaigns that connect with the consumer.

I have 12 years business experience in a realm of interesting fields form 11 years in coordinating international music festivals & promotions, 6 years in radio with 8 radio awards including a NZ radio award for best sales team in NZ and was the national brand and sales manager for New Zealands 1st indoor entertainment mall. With 10 years of experience in advertising sales, I have an eye for creating revenue streams for businesses and thrive on implementing campaigns that compliment those streams.

I love sayings like "Do what you love, love what you do" and believe that you can achieve anything you want.

I have been fortunate in my career that my connections have carried me without needing to promote my business however it is important that I start to do so.

Target Market(s)

Decision makers 25 to 54

Contact Information for Business Card

Petra Holsworth
Director
p. 022 739 5081
e. petra@brightkoru.example
www.brightkoru.example

FB, IG and Linkedin logo

Font styles to use
Sans Serif

Colors

Designer to choose colors to be used in the design.

Requirements
Must have
• Petra Holsworth
• Director
• p. 022 739 5081
• e. petra@brightkoru.example
• www.brightkoru.example
• FB, IG and Linkedin logo
Nice to have
• I am looking for a business card with character, that leaves my presence with my customer and makes them remember my brand & optimistic personality when i walk out the door.

```html
<!DOCTYPE html>
<html lang="en">
<head>
<meta charset="utf-8">
<title>Brightkoru NZ — Business Card</title>
<link rel="stylesheet" href="https://fonts.googleapis.com/css2?family=Roboto:wght@400;500;700&display=swap">
<style>
  :root {
    --page-bg: #e9e9e8;
    --card-light: #eeeeed;
    --card-dark: #2b2c2f;
    --brand-blue: #2a9fdb;
    --edge-blue: #2fa6e0;
    --text-grey: #9a9a9a;
    --rule-grey: #b9b9b9;
    --white: #ffffff;
  }
  * { box-sizing: border-box; margin: 0; padding: 0; }
  html, body { width: 1200px; height: 801px; overflow: hidden; }
  body {
    background: var(--page-bg);
    font-family: "Roboto", Arial, sans-serif;
    position: relative;
  }
  .card {
    position: absolute;
    width: 520px;
    height: 298px;
    border-bottom: 4px solid var(--edge-blue);
    box-shadow: 0 10px 24px rgba(0,0,0,0.12);
    overflow: hidden;
  }
  .card--front { left: 60px; top: 190px; background: var(--card-light); }
  .card--back  { left: 620px; top: 310px; background: var(--card-dark); }

  /* front */
  .brand {
    position: absolute;
    color: var(--brand-blue);
    font-weight: 700;
    letter-spacing: 0.04em;
    white-space: nowrap;
  }
  .front-brand { left: 40px; top: 128px; }
  .front-brand .brand-name { font-size: 27px; display: block; line-height: 1; }
  .front-brand .brand-tagline {
    display: block; margin-top: 5px; font-size: 8.4px; font-weight: 400;
    color: var(--text-grey); letter-spacing: 0.02em;
  }
  .divider {
    position: absolute; left: 262px; top: 70px; width: 1px; height: 110px;
    background: var(--rule-grey);
  }
  .contact { position: absolute; left: 290px; top: 66px; }
  .contact-name { color: var(--brand-blue); font-weight: 700; font-size: 18px; }
  .contact-role { color: var(--text-grey); font-size: 13px; margin-top: 2px; }
  .contact-list { list-style: none; margin-top: 16px; }
  .contact-list li {
    display: flex; align-items: center; gap: 9px;
    color: var(--text-grey); font-size: 13px; line-height: 21px;
  }
  .contact-list svg { width: 12px; height: 12px; flex: none; }
  .social { position: absolute; left: 400px; top: 234px; display: flex; gap: 8px; }
  .social span {
    width: 17px; height: 17px; border-radius: 3px; background: var(--brand-blue);
    display: block;
  }

  /* back */
  .back-feature {
    position: absolute; right: 0; top: 0; width: 300px; height: 298px;
    background: radial-gradient(ellipse at 85% 35%, #55565a 0%, #3a3b3f 45%, var(--card-dark) 80%);
  }
  .back-brand { left: 30px; top: 196px; }
  .back-brand .brand-name { font-size: 34px; display: block; line-height: 1; }
  .back-brand .brand-tagline {
    display: block; margin-top: 6px; font-size: 11px; font-weight: 500;
    color: var(--white); letter-spacing: 0.03em;
  }
</style>
</head>
<body>
  <section class="card card--front" aria-label="Business card front">
    <div class="brand front-brand">
      <span class="brand-name">BRIGHTKORU NZ</span>
      <span class="brand-tagline">BRAND | REVENUE | EVENTS &amp; PROMOTIONS</span>
    </div>
    <div class="divider"></div>
    <div class="contact">
      <p class="contact-name">Petra Holsworth</p>
      <p class="contact-role">Director</p>
      <ul class="contact-list">
        <li>
          <svg viewBox="0 0 12 12" aria-hidden="true"><path d="M2.5 1h2l1 2.5-1.3 1a6 6 0 0 0 3.3 3.3l1-1.3L11 7.5v2c0 .8-.7 1.5-1.5 1.5A8.5 8.5 0 0 1 1 2.5C1 1.7 1.7 1 2.5 1z" fill="var(--brand-blue)"/></svg>
          022 739 5081
        </li>
        <li>
          <svg viewBox="0 0 12 12" aria-hidden="true"><rect x="1" y="2.5" width="10" height="7" rx="1" fill="none" stroke="var(--brand-blue)" stroke-width="1.2"/><path d="M1.5 3l4.5 3.5L10.5 3" fill="none" stroke="var(--brand-blue)" stroke-width="1.2"/></svg>
          petra@brightkoru.example
        </li>
        <li>
          <svg viewBox="0 0 12 12" aria-hidden="true"><circle cx="6" cy="6" r="5" fill="none" stroke="var(--brand-blue)" stroke-width="1.1"/><ellipse cx="6" cy="6" rx="2.2" ry="5" fill="none" stroke="var(--brand-blue)" stroke-width="1"/><path d="M1 6h10" stroke="var(--brand-blue)" stroke-width="1"/></svg>
          www.brightkoru.example
        </li>
      </ul>
    </div>
    <div class="social" aria-label="Social media profiles">
      <span></span><span></span><span></span>
    </div>
  </section>

  <section class="card card--back" aria-label="Business card back">
    <div class="back-feature" role="img" aria-label="Large embossed brand symbol decoration"></div>
    <div class="brand back-brand">
      <span class="brand-name">BRIGHTKORU NZ</span>
      <span class="brand-tagline">BRAND | REVENUE | EVENTS &amp; PROMOTIONS</span>
    </div>
  </section>
</body>
</html>
```